Gah Phew Stinky washing machine cleaner label

We have just developed the most advance washing machine cleaner.
Gah Phew Washing Machine Cleaner. To learn more you can see our Gah Phew jetted tub cleaner on Brindlemart: http://www.brindlemart-example.com/Phew-Jetted-System-Cleaner-16oz/dp/Q4T7ZK2LMN/ref=sr_1_1?ie=UTF8&qid=1422631804&sr=8-1&keywords=gah+phew&pebp=1422631787362&peasin=Q4T7ZK2LMN
or our web site: http://www.quorvalenzymeworks-example.com/gah-phew-cleaner/

These ClipHarbor videos show our Gah Phew jetted tub cleaner: https://www.clipharbor-example.com/results?search_query=gah+phew

This new cleaner removes funky smell from washing machines

This product cleans the nasty slime that develops from leftover water in the washing machine. The leftover water is contaminated, that is why you notice a foul odor. It takes a specialized cleaner like Gah Phew to remove and clean this contamination. Your washing machine should be clean, safe, and odorless after using Gah Phew.

Feel free to incorporate clear into the design, or a standard label. Use the Gah Phew look but make it look like a washing machine cleaner. Use your imagination! The label should be 5" high and 3" wide.

Keep in mind the main selling point is to get consumers to use the product because they understand the concept to clean their washing machine removing the nasty contaminants that cause the foul odors.

Project Deadline Extended Reason: We are obtaining good designs but not quite perfect yet. We want the front label to sell what the product does and why consumers need to use it. Added Saturday, February 07, 2015

Project Deadline Extended
Reason: We have some nice designs but not quite what we want. We would like to have the washing machine represent clean inside the open door. We are leaning towards a clear label (the product inside is green).

Anyone with a washing machine

Learn

• We want to maintain our "Gah Phew" name.
• The label should sell our product and what it does in just a second or two. You don't have to have the warnings on the front label.
• We are open to creative design ideas that will help our label stand out. The label should sell the reason consumers should clean the musty nasty smell in their washing machines. Our cleaner will provide safer, cleaner, healthier loads of wash.
• Must use the "Gah Phew" name.

```html
<!DOCTYPE html>
<html lang="en">
<head>
<meta charset="utf-8">
<title>Gah Phew – Washing Machine Odor Remover Label</title>
<link href="https://fonts.googleapis.com/css2?family=Chewy&family=Kalam:wght@400;700&family=Varela+Round&family=Questrial&display=swap" rel="stylesheet">
<style>
  :root {
    --band-blue: #1b70b5;
    --title-blue: #1e78be;
    --sky-blue: #29abe2;
    --navy: #2d3a78;
    --brand-blue: #2e5fa3;
    --paper: #ffffff;
    --machine-light: #dfe6f6;
    --machine-mid: #8da3d8;
  }
  * { box-sizing: border-box; margin: 0; padding: 0; }
  html, body { width: 721px; height: 1200px; overflow: hidden; background: var(--paper); }
  .label { position: relative; width: 721px; height: 1200px; background: var(--paper); overflow: hidden; }

  .top-band { position: absolute; left: 0; top: 0; width: 100%; height: 40px; background: var(--band-blue); }

  .brand { position: absolute; left: 52px; top: 108px; display: flex; align-items: center; gap: 18px; }
  .brand-dot { width: 58px; height: 58px; border-radius: 50%; background: var(--brand-blue); }
  .brand-name { font-family: "Questrial", sans-serif; font-size: 46px; color: var(--brand-blue); letter-spacing: 0.5px; }

  .product-name {
    position: absolute; left: 0; top: 222px; width: 100%; text-align: center;
    font-family: "Chewy", cursive; font-size: 150px; line-height: 1; color: var(--title-blue);
  }

  .product-type {
    position: absolute; left: 84px; top: 432px; width: 516px; height: 120px;
    background: var(--sky-blue); border-radius: 10px 40px 12px 36px;
    display: flex; flex-direction: column; justify-content: center; align-items: center;
    font-family: "Kalam", cursive; font-weight: 700; font-size: 31px; line-height: 1.2;
    color: var(--navy); text-transform: uppercase; letter-spacing: 1px;
  }

  .claim { position: absolute; font-family: "Kalam", cursive; font-weight: 700; color: var(--navy); font-size: 31px; line-height: 1.35; transform: rotate(-8deg); }
  .claim-line { display: block; }
  .claim-odor { left: 108px; top: 612px; }
  .claim-odor .claim-line + .claim-line { padding-left: 36px; }
  .claim-residue { left: 84px; top: 742px; }
  .claim-residue .claim-line + .claim-line { padding-left: 10px; }

  .machine-illustration {
    position: absolute; left: 306px; top: 618px; width: 348px; height: 312px;
    border-radius: 14px;
    background: linear-gradient(150deg, var(--machine-light) 0%, #b7c5ea 55%, var(--machine-mid) 100%);
  }

  .usage-box {
    position: absolute; left: 78px; top: 954px; width: 542px; height: 140px;
    background: var(--sky-blue); border-radius: 18px;
    display: flex; align-items: center; justify-content: center; text-align: center;
    font-family: "Varela Round", sans-serif; font-size: 27px; line-height: 1.32; color: #2a2a3a;
  }

  .bottom-band {
    position: absolute; left: 0; top: 1116px; width: 100%; height: 84px; background: var(--band-blue);
    color: var(--paper); font-family: "Questrial", sans-serif;
    display: flex; align-items: center; justify-content: space-between; padding: 0 19px 0 22px;
  }
  .warning { font-size: 25px; letter-spacing: 0.3px; }
  .volume { font-size: 24px; text-align: right; line-height: 1.25; }
</style>
</head>
<body>
<main class="label">
  <div class="top-band"></div>

  <div class="brand">
    <span class="brand-dot"></span>
    <span class="brand-name">Quorval Enzyme Works</span>
  </div>

  <h1 class="product-name">Gah Phew</h1>

  <div class="product-type">
    <span>Washing Machine</span>
    <span>Odor Remover</span>
  </div>

  <p class="claim claim-odor"><span class="claim-line">No More</span><span class="claim-line">ODOR</span></p>
  <p class="claim claim-residue"><span class="claim-line">No More</span><span class="claim-line">RESIDUE</span></p>

  <div class="machine-illustration" role="img" aria-label="Illustration of a front-loading washing machine with a crossed-out odor cloud and flies beside its door"></div>

  <p class="usage-box">Use regularly to keep unhealthy<br>residue and bad odor away from<br>your washing machine</p>

  <footer class="bottom-band">
    <span class="warning">KEEP OUT OF REACH OF CHILDREN</span>
    <span class="volume">16 fl. oz<br>(464 ml)</span>
  </footer>
</main>
</body>
</html>
```